The RVH Relational Philanthropy Cycle

The title for this graphic is above. It must be included.
I am looking for a graphic representation of the relationship between the Christian school and the donor / pointing to the child (student) - the school's mission / outcome of investment through a gift / appreciation of the gift / communication of the gift impact for the child / stronger relationship going back to the child. This is not easy to do. I've tried to do it on my own and can't get it.
Any cliched child representations will be dismissed out of hand e.g. mortar boards, pencils, uniforms etc. The child should be abstract so that gender and race are irrelevant.
The key to this whole thing is the idea of RELATIONSHIP. The close relationship of donor and the Christian school, the pointing of that relationship to focus on the child / the school's mission, the outpouring of generosity that then happens in the heart of the donor and the gift that results, followed up by intentional work by the Christian school to thank and inform the donor - thank for the gift inform about the gift's expenditure and impact in the life of the child - all of which leads to a strengthening of the relationship and continued philanthropy as a never ending cycle.
It must be branded - logo and colors attached.
It must be obvious - easy to grasp the basic idea of relationship resulting in generosity / philanthropy. The visual should be clear - any words used illustrate - I should not 'need' the words to understand the idea.
I need it on a PP slide, jpeg, thumbnail. It must be highly legible in no more than 1/3 of a regular size piece of paper.
Our website is brightfieldacademyguild.org
google donor cultivation cycle or donor giving cycle to see many examples of cycles that are used in secular contexts - the big difference in RVH's is the focus on the child and the importance of the relationship.

```html
<!DOCTYPE html>
<html lang="en">
<head>
<meta charset="utf-8">
<title>The RVH Relational Philanthropy Cycle</title>
<link rel="stylesheet" href="https://fonts.googleapis.com/css2?family=Crimson+Pro:wght@600&family=Montserrat:wght@500;700&display=swap">
<style>
  :root {
    --brand-blue: #3f72a8;
    --brand-navy: #2e5f92;
    --title-grey: #7f7f80;
    --ring-light: #d9d9d9;
    --ring-dark: #a8a8a8;
    --ink: #111111;
    --paper: #ffffff;
  }
  html, body {
    margin: 0;
    padding: 0;
    width: 1200px;
    height: 808px;
    overflow: hidden;
    background: var(--paper);
  }
  .cycle-graphic {
    display: block;
    width: 1200px;
    height: 808px;
  }
  .title { font-family: "Crimson Pro", Georgia, serif; font-weight: 600; font-size: 20px; fill: var(--title-grey); }
  .title-lead { fill: var(--brand-navy); }
  .brand-name { font-family: "Montserrat", Arial, sans-serif; font-weight: 700; font-size: 24px; fill: var(--brand-blue); }
  .brand-dot { fill: var(--brand-blue); }
  .node { fill: var(--brand-blue); }
  .node-label { font-family: "Montserrat", Arial, sans-serif; font-weight: 700; font-size: 11.5px; fill: var(--paper); text-anchor: middle; }
  .icon { fill: none; stroke: var(--paper); stroke-width: 1.4; stroke-linejoin: round; stroke-linecap: round; }
  .arc-label { font-family: "Montserrat", Arial, sans-serif; font-weight: 500; font-size: 12.5px; fill: var(--brand-blue); }
  .inner-label { font-family: "Montserrat", Arial, sans-serif; font-weight: 500; font-size: 12px; fill: var(--ink); }
  .disc { fill: var(--ring-light); }
  .flow-arc { fill: none; stroke: var(--ring-dark); stroke-width: 20; }
  .flow-head { fill: var(--ring-dark); }
  .ring-inner { fill: none; stroke: var(--ring-light); stroke-width: 18; }
  .ring-outer { fill: none; stroke: var(--ring-dark); stroke-width: 13; }
  .link-arrow { fill: var(--paper); }
</style>
</head>
<body>
<svg class="cycle-graphic" viewBox="0 0 750 505" xmlns="http://www.w3.org/2000/svg" role="img" aria-label="The RVH Relational Philanthropy Cycle: donor, child and Christian school in a continuing cycle of generosity and impact">
  <defs>
    <symbol id="icon-donor" viewBox="0 0 40 40">
      <path class="icon" d="M20 17 C14 12 12 6 16 4 C18 3 20 5 20 7 C20 5 22 3 24 4 C28 6 26 12 20 17 Z"/>
      <path class="icon" d="M6 24 L12 22 C15 21 18 22 20 24 L25 24 C27 24 27 27 25 27 L18 27 M6 32 L13 30 L24 31 C26 31 28 30 30 28 L35 22 C36 20 34 19 32 20 L27 24"/>
    </symbol>
    <symbol id="icon-child" viewBox="0 0 40 40">
      <circle class="icon" cx="20" cy="8" r="3.5"/>
      <rect class="icon" x="16.5" y="14" width="7" height="20" rx="3.5"/>
      <circle class="icon" cx="9" cy="11" r="3"/>
      <rect class="icon" x="6" y="16" width="6" height="17" rx="3"/>
      <circle class="icon" cx="31" cy="11" r="3"/>
      <rect class="icon" x="28" y="16" width="6" height="17" rx="3"/>
    </symbol>
    <symbol id="icon-school" viewBox="0 0 40 40">
      <path class="icon" d="M20 1 V7 M17.5 3.5 H22.5"/>
      <path class="icon" d="M12 17 L20 8 L28 17 V36 H12 Z"/>
      <path class="icon" d="M4 36 V22 H12 M28 22 H36 V36 M2 36 H38"/>
      <path class="icon" d="M17 36 V28 H23 V36"/>
    </symbol>

    <path id="left-top-text" d="M28 268 A152 152 0 0 1 332 268"/>
    <path id="left-bottom-text" d="M22 268 A158 158 0 0 0 338 268"/>
    <path id="left-inner-top" d="M107 268 A73 73 0 0 1 253 268"/>
    <path id="left-inner-bottom" d="M98 268 A82 82 0 0 0 262 268"/>

    <path id="right-top-text" d="M338 268 A162 162 0 0 1 662 268"/>
    <path id="right-bottom-text" d="M332 268 A168 168 0 0 0 668 268"/>
    <path id="right-inner-top" d="M415 268 A85 85 0 0 1 585 268"/>
    <path id="right-inner-bottom" d="M406 268 A94 94 0 0 0 594 268"/>
  </defs>

  <!-- Header -->
  <text class="title" x="28" y="82"><tspan class="title-lead">The RVH</tspan> Relational Philanthropy Cycle</text>
  <g class="brand">
    <circle class="brand-dot" cx="628" cy="64" r="7"/>
    <text class="brand-name" x="642" y="73">RVH</text>
  </g>

  <!-- Cycle A: open arrows -->
  <g class="cycle cycle-arrows">
    <circle class="disc" cx="180" cy="268" r="100"/>
    <path class="flow-arc" d="M72 201 A127 127 0 0 1 273 182"/>
    <polygon class="flow-head" points="285,171 255,199 292,207"/>
    <path class="flow-arc" d="M288 335 A127 127 0 0 1 87 354"/>
    <polygon class="flow-head" points="102,340 72,368 66,332"/>

    <text class="arc-label" text-anchor="middle"><textPath href="#left-top-text" startOffset="50%">Outpouring Of Generosity</textPath></text>
    <text class="arc-label" text-anchor="middle"><textPath href="#left-bottom-text" startOffset="50%">Impact In The Life Of The Child</textPath></text>
    <text class="inner-label" text-anchor="middle"><textPath href="#left-inner-top" startOffset="50%">Focus On The Child</textPath></text>
    <text class="inner-label" text-anchor="middle"><textPath href="#left-inner-bottom" startOffset="50%">The School's Mission</textPath></text>

    <g class="node-donor">
      <circle class="node" cx="70" cy="268" r="52"/>
      <use href="#icon-donor" x="56" y="236" width="28" height="28"/>
      <text class="node-label" x="70" y="298">DONOR</text>
    </g>
    <g class="node-child">
      <circle class="node" cx="180" cy="268" r="52"/>
      <use href="#icon-child" x="165" y="246" width="30" height="30"/>
      <text class="node-label" x="180" y="298">THE CHILD</text>
    </g>
    <g class="node-school">
      <circle class="node" cx="290" cy="268" r="52"/>
      <use href="#icon-school" x="276" y="236" width="28" height="28"/>
      <text class="node-label" x="290" y="292">CHRISTIAN</text>
      <text class="node-label" x="290" y="306">SCHOOL</text>
    </g>

    <polygon class="link-arrow" points="112,268 122,258 122,264 128,264 128,258 138,268 128,278 128,272 122,272 122,278"/>
    <polygon class="link-arrow" points="222,268 232,258 232,264 238,264 238,258 248,268 238,278 238,272 232,272 232,278"/>
  </g>

  <!-- Cycle B: continuous rings -->
  <g class="cycle cycle-rings">
    <path class="ring-outer" d="M382 192 A142 142 0 0 1 612 180"/>
    <path class="ring-outer" d="M618 344 A142 142 0 0 1 388 356"/>
    <path class="ring-inner" d="M396 203 A122 122 0 0 1 598 195"/>
    <path class="ring-inner" d="M604 333 A122 122 0 0 1 402 341"/>

    <text class="arc-label" text-anchor="middle"><textPath href="#right-top-text" startOffset="50%">Outpouring Of Generosity</textPath></text>
    <text class="arc-label" text-anchor="middle"><textPath href="#right-bottom-text" startOffset="50%">Impact In The Life Of The Child</textPath></text>
    <text class="inner-label" text-anchor="middle"><textPath href="#right-inner-top" startOffset="50%">Focus On The Child</textPath></text>
    <text class="inner-label" text-anchor="middle"><textPath href="#right-inner-bottom" startOffset="50%">The School's Mission</textPath></text>

    <g class="node-donor">
      <circle class="node" cx="414" cy="268" r="52"/>
      <use href="#icon-donor" x="400" y="236" width="28" height="28"/>
      <text class="node-label" x="414" y="298">DONOR</text>
    </g>
    <g class="node-child">
      <circle class="node" cx="524" cy="268" r="52"/>
      <use href="#icon-child" x="509" y="246" width="30" height="30"/>
      <text class="node-label" x="524" y="298">THE CHILD</text>
    </g>
    <g class="node-school">
      <circle class="node" cx="634" cy="268" r="52"/>
      <use href="#icon-school" x="620" y="236" width="28" height="28"/>
      <text class="node-label" x="634" y="292">CHRISTIAN</text>
      <text class="node-label" x="634" y="306">SCHOOL</text>
    </g>

    <polygon class="link-arrow" points="458,264 476,264 476,256 486,264 486,266 458,266"/>
    <polygon class="link-arrow" points="488,272 470,272 470,280 460,272 460,270 488,270"/>
    <polygon class="link-arrow" points="568,264 586,264 586,256 596,264 596,266 568,266"/>
    <polygon class="link-arrow" points="598,272 580,272 580,280 570,272 570,270 598,270"/>
  </g>
</svg>
</body>
</html>
```